Business Cards

Business cards (double-sided) to be handed out to clients and potential clients, with contact details, logo .

Target Market(s)

Small to medium size businesses

Industry/Entity Type

Accountants

Contact Information for Business Card

Brightwater Ledger & Counsel Ltd

Colors

Designer to choose only greyscale colors for use in the design.

Requirements
Must have
• Name, Title, Address, Phone number, Email, Website
Nice to have
• Modern, clean lines, classy
Should not have
• Business cards to be double-sided. Form keeps reverting to single-sided.

```html
<!DOCTYPE html>
<html lang="en">
<head>
<meta charset="utf-8">
<title>Brightwater Ledger &amp; Counsel Ltd — Business Card</title>
<link rel="stylesheet" href="https://fonts.googleapis.com/css2?family=Josefin+Sans:wght@300;400&display=swap">
<style>
  :root {
    --page-bg: #e6e7e9;
    --card-bg: #000000;
    --ink: #ffffff;
  }
  * { margin: 0; padding: 0; box-sizing: border-box; }
  html, body {
    width: 1200px;
    height: 1200px;
    overflow: hidden;
    background: var(--page-bg);
  }
  .canvas {
    position: relative;
    width: 1200px;
    height: 1200px;
  }
  .card {
    position: absolute;
    left: 236px;
    width: 728px;
    height: 440px;
    background: var(--card-bg);
    color: var(--ink);
    font-family: "Josefin Sans", sans-serif;
  }
  .card--front { top: 129px; }
  .card--back { top: 631px; }

  .front-name {
    position: absolute;
    inset: 0;
    display: flex;
    flex-direction: column;
    align-items: center;
    justify-content: center;
    text-align: center;
    font-weight: 400;
    font-size: 34px;
    line-height: 1.35;
    letter-spacing: 0.12em;
    text-transform: uppercase;
  }

  .contact-table { display: block; width: 728px; height: 440px; }
  .contact-table .rule { stroke: var(--ink); stroke-width: 3; fill: none; }
  .contact-table text {
    fill: var(--ink);
    font-family: "Josefin Sans", sans-serif;
    font-weight: 300;
    text-anchor: middle;
  }
  .contact-table .person-name { font-size: 44px; font-weight: 400; }
  .contact-table .person-title,
  .contact-table .detail { font-size: 32px; letter-spacing: 0.03em; }
  .contact-table .phone-area { font-size: 62px; }
  .contact-table .phone-number { font-size: 50px; }
</style>
</head>
<body>
<main class="canvas">
  <section class="card card--front" aria-label="Card front">
    <h1 class="front-name">
      <span>Brightwater Ledger</span>
      <span>&amp; Counsel Ltd</span>
    </h1>
  </section>

  <section class="card card--back" aria-label="Card back">
    <svg class="contact-table" viewBox="0 0 1170 706" xmlns="http://www.w3.org/2000/svg">
      <g class="rule">
        <rect x="150" y="165" width="870" height="375"/>
        <line x1="620" y1="165" x2="620" y2="353"/>
        <line x1="620" y1="446" x2="620" y2="540"/>
        <line x1="150" y1="259" x2="620" y2="259"/>
        <line x1="150" y1="353" x2="1020" y2="353"/>
        <line x1="150" y1="446" x2="1020" y2="446"/>
      </g>
      <text class="person-name" x="385" y="228">YOUR NAME</text>
      <text class="person-title" x="385" y="318">Your Designation</text>
      <text class="phone-area" x="820" y="252">(800)</text>
      <text class="phone-number" x="820" y="322">123-4567</text>
      <text class="detail" x="585" y="410">Your Company Address Here</text>
      <text class="detail" x="385" y="503">Your Email Address</text>
      <text class="detail" x="820" y="503">Your Website</text>
    </svg>
  </section>
</main>
</body>
</html>
```